President
General Contractor
I need single sided standard sized Business Card [3.5" x 2"]
I am open to ideas
Simple
Darnell Whitby
President/CEO
P.O. Box 7413
Orangeburg, South Carolina 29116
darnell@keystrelbuilderssc.example
www.keystrelbuilderssc.example
K573841 and R408657
Designers, you may want to check out my website. wwwkeystrelbuilderssc.example I have a log that Iam not crazy about. I want it to reflect more about residential and commerical construction, development and construction management.
I am open to using the back of the card.
Company's Logo

```html
<!DOCTYPE html>
<html lang="en">
<head>
<meta charset="utf-8">
<title>Keystrel Builders – Business Card</title>
<link rel="stylesheet" href="https://fonts.googleapis.com/css2?family=Open+Sans:wght@400;700&display=swap">
<style>
  :root {
    --backdrop: #e9e6e2;
    --card: #ffffff;
    --brand-red: #8e0f12;
    --rule-grey: #9a9a9a;
    --ink: #2b2b2b;
    --on-red: #ffffff;
  }
  * { margin: 0; padding: 0; box-sizing: border-box; }
  html, body {
    width: 1200px; height: 780px; overflow: hidden;
    background: var(--backdrop);
    font-family: "Open Sans", Arial, sans-serif;
  }
  .card {
    position: absolute; left: 75px; top: 90px;
    width: 1050px; height: 600px;
    background: var(--card);
    border-radius: 34px;
    box-shadow: 0 10px 30px rgba(0,0,0,.18);
    overflow: hidden;
  }
  .rule {
    position: absolute; left: 0; right: 0; height: 3px;
    background: var(--rule-grey);
  }
  .rule--top { top: 74px; }
  .rule--bottom { top: 188px; }
  .band {
    position: absolute; left: 0; right: 0; top: 84px; height: 96px;
    background: var(--brand-red);
  }
  .holder {
    position: absolute; right: 80px; top: 100px;
    text-align: right; color: var(--on-red);
  }
  .holder__name { font-weight: 700; font-size: 30px; line-height: 1.15; }
  .holder__title { font-weight: 700; font-size: 18px; line-height: 1.3; }
  .brand {
    position: absolute; left: 60px; top: 40px;
    display: flex; flex-direction: column; gap: 26px;
  }
  .brand__square {
    width: 150px; height: 150px;
    background: var(--brand-red);
    border: 6px solid var(--card);
  }
  .brand__name {
    color: var(--ink);
    font-weight: 700; font-size: 30px; line-height: 1.2;
    white-space: nowrap;
  }
  .contact {
    position: absolute; left: 60px; top: 372px;
    color: var(--ink); font-size: 21px; line-height: 1.2;
  }
  .contact__row { display: flex; align-items: center; gap: 24px; margin-bottom: 14px; }
  .contact__item { display: flex; align-items: center; gap: 6px; }
  .icon { width: 20px; height: 20px; flex: none; }
</style>
</head>
<body>
  <main class="card">
    <div class="rule rule--top"></div>
    <div class="band"></div>
    <div class="rule rule--bottom"></div>

    <div class="holder">
      <p class="holder__name">Darnell Whitby</p>
      <p class="holder__title">President/CEO</p>
    </div>

    <div class="brand">
      <div class="brand__square"></div>
      <p class="brand__name">Keystrel Builders</p>
    </div>

    <div class="contact">
      <p class="contact__row">P.O. Box 7413 Orangeburg, South Carolina 29116</p>
      <div class="contact__row">
        <span class="contact__item">
          <svg class="icon" viewBox="0 0 20 20"><path d="M4 2 L8 2 L9 6 L7 8 Q9 12 12 13 L14 11 L18 12 L18 16 Q10 18 4 10 Q2 6 4 2Z" fill="#8e0f12"/></svg>
          803-555-0142
        </span>
        <span class="contact__item">
          <svg class="icon" viewBox="0 0 20 20"><rect x="5" y="1" width="10" height="18" rx="2" fill="#8e0f12"/><rect x="7" y="4" width="6" height="9" fill="#fff"/></svg>
          803-555-0187
        </span>
        <span class="contact__item">
          <svg class="icon" viewBox="0 0 20 20"><rect x="2" y="8" width="16" height="9" rx="1" fill="#8e0f12"/><rect x="5" y="2" width="10" height="7" fill="#8e0f12"/><rect x="6" y="3" width="8" height="5" fill="#fff"/></svg>
          803-555-0119
        </span>
      </div>
      <p class="contact__row contact__item">
        <svg class="icon" viewBox="0 0 20 20"><circle cx="10" cy="10" r="9" fill="#8e0f12"/><circle cx="10" cy="10" r="3.5" fill="none" stroke="#fff" stroke-width="2"/></svg>
        darnell@keystrelbuilderssc.example
      </p>
      <p class="contact__row contact__item">
        <svg class="icon" viewBox="0 0 20 20"><circle cx="10" cy="10" r="9" fill="#8e0f12"/><path d="M1 10 H19 M10 1 Q5 10 10 19 M10 1 Q15 10 10 19" stroke="#fff" stroke-width="1.3" fill="none"/></svg>
        www.keystrelbuilderssc.example
      </p>
    </div>
  </main>
</body>
</html>
```